We sell companies excess stock for them

We need a business card for a company based in New Zealand called 'StockHarbor'.

Check out our website to get an idea www.stockharbor.example

We help other businesses to;
- Sell Excess Stock
- Manage Product Returns
- Sell Company Assets

Our logo is attached for your reference
The font used is 'RifficFree-Bold'

Target Market(s)

Businesses

Industry/Entity Type

Business

Contact Information for Business Card

Name: Mark Pellow
Phone: 027 846 2093
email: markpellow@stockharbor.example
website: www.stockharbor.example

Font styles to use
Other font styles liked:
• Unsure

Colors
9bcb3b

Requirements
Must have
• coming soon
Nice to have
• coming soon
Should not have
• coming soon

```html
<!DOCTYPE html>
<html lang="en">
<head>
<meta charset="utf-8">
<title>StockHarbor Business Card</title>
<link href="https://fonts.googleapis.com/css2?family=Montserrat:wght@700;800&family=Raleway:wght@400;500;800&display=swap" rel="stylesheet">
<style>
  :root {
    --stage: #1c1d1d;
    --brand-green: #9bcb3b;
    --green-light: #93c83e;
    --green-deep: #64a22f;
    --ink: #2a2a2a;
    --ink-soft: #3a3a36;
    --paper: #fbf9fb;
    --band: #343231;
    --white: #ffffff;
    --figure-green: #5fae3a;
    --figure-orange: #f0a030;
  }
  * { box-sizing: border-box; margin: 0; padding: 0; }
  html, body { width: 1200px; height: 1000px; overflow: hidden; background: var(--stage); }
  .stage { position: relative; width: 1200px; height: 1000px; }

  .card {
    position: absolute;
    left: 240px;
    width: 720px;
    height: 410px;
    border-radius: 42px;
    overflow: hidden;
    box-shadow: 0 14px 30px rgba(0,0,0,0.45);
  }

  /* Back */
  .card--back {
    top: 60px;
    background: radial-gradient(ellipse at 40% 50%, var(--green-light) 0%, #7fb836 45%, var(--green-deep) 100%);
  }
  .tagline {
    position: absolute; left: 70px; top: 66px;
    font-family: 'Raleway', sans-serif; font-weight: 500; font-size: 24px;
    color: var(--ink-soft);
  }
  .tagline strong { color: var(--white); font-weight: 800; }
  .services {
    position: absolute; left: 70px; top: 112px; list-style: none;
    font-family: 'Raleway', sans-serif; font-weight: 500; font-size: 22px;
    color: var(--ink-soft);
  }
  .services li { display: flex; align-items: center; gap: 12px; height: 34px; }
  .services svg { width: 22px; height: 18px; flex: none; }

  .wordmark {
    position: absolute;
    font-family: 'Montserrat', sans-serif; font-weight: 800;
    letter-spacing: -1.5px; color: var(--ink);
  }
  .card--back .wordmark { left: 66px; bottom: 62px; font-size: 52px; }

  .mascot {
    position: absolute;
    border-radius: 28px;
    background: linear-gradient(160deg, var(--figure-green) 0%, #8cc640 55%, var(--figure-orange) 100%);
    opacity: 0.9;
  }
  .card--back .mascot { left: 480px; top: 70px; width: 200px; height: 290px; }

  /* Front */
  .card--front { top: 530px; background: var(--paper); }
  .holder { position: absolute; left: 70px; top: 50px; }
  .holder__name {
    font-family: 'Montserrat', sans-serif; font-weight: 800; font-size: 40px;
    color: var(--brand-green); text-transform: uppercase; letter-spacing: -0.5px; line-height: 1;
  }
  .holder__role {
    font-family: 'Montserrat', sans-serif; font-weight: 700; font-size: 22px;
    color: var(--ink); margin-top: 4px;
  }
  .contacts {
    position: absolute; left: 70px; top: 168px; list-style: none;
    font-family: 'Raleway', sans-serif; font-weight: 400; font-size: 21px; color: var(--ink);
  }
  .contacts li { display: flex; align-items: center; gap: 14px; height: 34px; }
  .contacts svg { width: 22px; height: 22px; flex: none; }

  .band {
    position: absolute; left: 0; top: 296px; width: 360px; height: 42px;
    background: var(--band);
  }
  .card--front .wordmark { left: 384px; top: 290px; font-size: 42px; }
  .card--front .mascot { left: 470px; top: 40px; width: 200px; height: 235px; }
</style>
</head>
<body>
<main class="stage">

  <section class="card card--back">
    <p class="tagline"><strong>We help</strong> other businesses to:</p>
    <ul class="services">
      <li><svg viewBox="0 0 22 18"><path d="M2 10 L8 15 L20 3" fill="none" stroke="#fff" stroke-width="3" stroke-linecap="round" stroke-linejoin="round"/></svg>Sell Excess Stock</li>
      <li><svg viewBox="0 0 22 18"><path d="M2 10 L8 15 L20 3" fill="none" stroke="#fff" stroke-width="3" stroke-linecap="round" stroke-linejoin="round"/></svg>Manage Product Returns</li>
      <li><svg viewBox="0 0 22 18"><path d="M2 10 L8 15 L20 3" fill="none" stroke="#fff" stroke-width="3" stroke-linecap="round" stroke-linejoin="round"/></svg>Sell Company Assets</li>
    </ul>
    <div class="wordmark">StockHarbor</div>
    <div class="mascot" role="img" aria-label="Cartoon mascot of a running delivery worker in a green cap and overalls carrying an orange parcel"></div>
  </section>

  <section class="card card--front">
    <div class="holder">
      <h1 class="holder__name">Mark Pellow</h1>
      <p class="holder__role">Owner</p>
    </div>
    <ul class="contacts">
      <li><svg viewBox="0 0 24 24"><path d="M6 2 L10 2 L11 7 L8.5 9 C9.5 11.5 12.5 14.5 15 15.5 L17 13 L22 14 L22 18 C22 20 20 22 18 22 C9 21 3 15 2 6 C2 4 4 2 6 2 Z" fill="none" stroke="var(--brand-green)" stroke-width="2" stroke-linejoin="round"/></svg>027 846 2093</li>
      <li><svg viewBox="0 0 24 24"><rect x="2" y="5" width="20" height="14" rx="1.5" fill="none" stroke="var(--brand-green)" stroke-width="2"/><path d="M2 6 L12 13 L22 6" fill="none" stroke="var(--brand-green)" stroke-width="2"/></svg>markpellow@stockharbor.example</li>
      <li><svg viewBox="0 0 24 24"><circle cx="12" cy="12" r="10" fill="var(--brand-green)"/><path d="M2 12 H22 M12 2 C7 7 7 17 12 22 M12 2 C17 7 17 17 12 22 M4 7 H20 M4 17 H20" fill="none" stroke="var(--paper)" stroke-width="1.4"/></svg>www.stockharbor.example</li>
    </ul>
    <div class="band"></div>
    <div class="wordmark">StockHarbor</div>
    <div class="mascot" role="img" aria-label="Cartoon mascot of a running delivery worker in a green cap and overalls carrying an orange parcel"></div>
  </section>

</main>
</body>
</html>
```